Business Card for a New Zealand IT Startup

I need a business card for Talmor Ventures. We are a young startup based in New Zealand working in internet marketing and web development. The design should have some element connected to New Zealand, such as wave, koru or silver fern, just don't use a kiwi bird.

```html
<!DOCTYPE html>
<html lang="en">
<head>
<meta charset="utf-8">
<title>Talmor Ventures – Business Card</title>
<link rel="stylesheet" href="https://fonts.googleapis.com/css2?family=Open+Sans:wght@400;600;700&display=swap">
<style>
  :root {
    --backdrop: #e9e7e4;
    --card-dark: #17191c;
    --card-light: #ececec;
    --silver: #c9cbce;
    --silver-dim: #8e9297;
    --brand-blue: #1a73c2;
    --accent-orange: #f0622c;
    --ink: #4a4a4a;
    --rule: #6f6f6f;
  }
  * { box-sizing: border-box; margin: 0; padding: 0; }
  html, body { width: 1200px; height: 864px; overflow: hidden; }
  body {
    background: var(--backdrop);
    font-family: "Open Sans", Arial, sans-serif;
    display: flex;
    flex-direction: column;
    align-items: center;
    justify-content: center;
    gap: 40px;
  }
  .card {
    position: relative;
    width: 660px;
    height: 377px;
    border-radius: 4px;
    box-shadow: 0 6px 18px rgba(0,0,0,0.18);
    overflow: hidden;
  }

  /* Front */
  .card--front { background: var(--card-dark); }
  .card--front .wordmark {
    position: absolute;
    left: 90px;
    top: 120px;
    display: flex;
    align-items: center;
    gap: 18px;
  }
  .card--front .wordmark-text {
    font-size: 50px;
    font-weight: 700;
    color: var(--silver);
    letter-spacing: 1px;
  }
  .card--front .wordmark-dot {
    width: 54px; height: 54px;
    border-radius: 50%;
    background: #2a2d31;
  }
  .card--front .site {
    position: absolute;
    left: 92px;
    top: 226px;
    font-size: 16px;
    letter-spacing: 5px;
    color: var(--silver);
  }

  /* Back */
  .card--back { background: var(--card-light); }
  .person {
    position: absolute;
    left: 40px;
    top: 118px;
  }
  .person-name {
    font-size: 25px;
    font-weight: 700;
    color: var(--brand-blue);
    line-height: 1;
  }
  .person-title {
    font-size: 15px;
    color: var(--accent-orange);
    text-transform: uppercase;
    margin-top: 2px;
  }
  .divider {
    position: absolute;
    left: 40px;
    right: 40px;
    top: 178px;
    height: 1px;
    background: var(--rule);
  }
  .contacts {
    position: absolute;
    left: 40px;
    top: 192px;
    list-style: none;
  }
  .contacts li {
    display: flex;
    align-items: center;
    gap: 8px;
    font-size: 15px;
    color: var(--ink);
    line-height: 24px;
  }
  .contacts svg { width: 14px; height: 14px; fill: var(--brand-blue); flex: none; }
  .card--back .wordmark {
    position: absolute;
    right: 40px;
    top: 86px;
    display: flex;
    align-items: center;
    gap: 12px;
  }
  .card--back .wordmark-text {
    font-size: 36px;
    font-weight: 700;
    color: var(--brand-blue);
  }
  .card--back .wordmark-dot {
    width: 38px; height: 38px;
    border-radius: 50%;
    background: var(--brand-blue);
  }
  .address {
    position: absolute;
    right: 40px;
    bottom: 36px;
    text-align: right;
    font-size: 16px;
    color: var(--ink);
    line-height: 23px;
  }
</style>
</head>
<body>

  <section class="card card--front" aria-label="Card front">
    <div class="wordmark">
      <span class="wordmark-text">Talmor Ventures</span>
      <span class="wordmark-dot"></span>
    </div>
    <p class="site">www.talmorventures.co.nz</p>
  </section>

  <section class="card card--back" aria-label="Card back">
    <div class="person">
      <p class="person-name">ARIA WHITLOW</p>
      <p class="person-title">President</p>
    </div>

    <div class="wordmark">
      <span class="wordmark-text">Talmor Ventures</span>
      <span class="wordmark-dot"></span>
    </div>

    <div class="divider"></div>

    <ul class="contacts">
      <li>
        <svg viewBox="0 0 16 16" aria-hidden="true"><path d="M3 1l3 3-2 2c1 2 3 4 5 5l2-2 3 3-2 2C7 14 2 9 1 3z"/></svg>
        021 448 3190
      </li>
      <li>
        <svg viewBox="0 0 16 16" aria-hidden="true"><path d="M4 0h8v16H4zM5.5 2v10h5V2zM7 13.5h2v1H7z" fill-rule="evenodd"/></svg>
        027 615 9042
      </li>
      <li>
        <svg viewBox="0 0 16 16" aria-hidden="true"><path d="M4 1h8v4H4zM1 6h14v6h-3v3H4v-3H1zM5 10v3h6v-3z" fill-rule="evenodd"/></svg>
        09 372 8164
      </li>
      <li>
        <svg viewBox="0 0 16 16" aria-hidden="true"><path d="M1 3h14v10H1zM2 4.5v.5l6 4 6-4v-.5z" fill-rule="evenodd"/></svg>
        aria@talmorventures.co.nz
      </li>
    </ul>

    <address class="address" style="font-style:normal">
      42 Harbourview Road<br>
      Ponsonby, Auckland 1011<br>
      www.talmorventures.co.nz
    </address>
  </section>

</body>
</html>
```